Kids painting app needs in-app icons

Need a set of in-app icons for a kids painting app. There are currently place-holder icons in place, but these icons are inconsistent and quite dull for a kids app.

Specifically we need 7 icons and a design for a slider.

***********************************************************************************************
See the "Nice to Haves" section below for updated comments to this brief.

We are looking for icons that are playful, but also don't want them to be overbearing, since the intent of the app is to focus on the painting experience itself, so limiting visual clutter is one of the core design goals.

We also want to avoid words as icons, since the intention is to localise the app in to a number of different languages, and we want to avoid the need to localise the icons themselves.

See the attached images for reference to the current placeholder layout. We do not what to spend too much time adjusting the current layout at present, but feel free to play around with your layout when presenting your work in place if you feel it significantly enhances the painting app overall.

You can try out the app on a recent iOS device by signing up to the alpha testing program from our web-site - www.brightdabstudio.com

Regards,
Kim

Target Market(s)

Painting app designed specifically for kids

Colors

Designer to choose colors to be used in the design.

Requirements
Must have
• The required elements are as follows:
• * Clean brush icon
• Tapping this icon will clean the paint off of the brush. This is currently being represented by the head of a brush, which we believe is quite appropriate, but if you feel there is a better way to represent this action we are open to suggestions.
• A design idea may be to have two variations of this icon: one with paint on the brush and one without paint on the brush. It would then be possible to display, or perhaps even blend between these two images to highlight the build up of paint on the brush, but primarily to highlight the purpose of the icon by giving visual feedback after pressing the icon
• * Options icon
• This is currently being represented by a gear icon. The option icon and the clean brush icon are the only two UI elements that are always visible. This icon simply shows / hides the final three additional icons
• * Share icon
• This icon is based on the standard iOS share icon, which launches the standard iOS share dialog. Any suggestions on a more kids friendly design are welcome, but feel free to include a design based off of the standard share icon if you feel it is still the most appropriate icon design to use
• * Return to Gallery
• We are currently using a green tick icon to represent this operation. Some of the thought process behind this icon was that we were also saving the image as we returned to the gallery, however saving will now happen automatically after each brush stroke, so that mental concept has been relaxed.
• * Reset Painting
• We are currently using a red X icon to represent this operation. This allows you to clear the canvas, clean the brush, and reset the paint palette all with a single icon press.
• * Undo / Redo
• While not implemented at present, we may implement undo / redo functionality in the future, so we would like icon designs for these. Also, having to include designs for undo and redo will like influence how you design the Return to Gallery icon, in order to differentiate the operations.
• There is also one more visual element that need further attention, but isn't exactly an icon:
• * Brush width slider
• After performing a long press on the clean brush icon, the brush width slider appears. This is currently using a standard iOS slider. Note that ideally this slider should not always be visible, in order to limit on-screen clutter, but it is also important for it to be easily discoverable and intuitive to use.
• Side note:
• It is straight-forward to tint any white icons inside iOS, so icons can be created in grey scale and coloured inside the app. However, if your design has a specific colour theme please provide both grey scale and full colour versions to make it easy for use to possibly offer different colour themes inside the app at a later date.
Nice to have
• ***********************************************************************************************
• UPDATE: 23 May - Consistency with logo
• Firstly, thank you to everyone who has already submitted a design. Seeing
• the variation in design makes it a lot easier for us to figure out our intended
• direction.
• I have uploaded two additional images of our P logo, and how it is integrated into the Dabwell Kids logo. Also, you may have noticed that the palette is rounded with circular paint swatches.
• We would like this rounded / circular theme to be a part of the icon designs also. This could mean having a rounded / circular background outline or rounded / circular features of the icon itself.
• Having the outline of the icons themselves appearing as if painted is something we are interested in exploring, similar to the P logo itself but probably greyscale or outlined
• Having seen a number of designs we are gravitating towards cleaner designs, either black and white or using just a single colour

```html
<!DOCTYPE html>
<html lang="en">
<head>
<meta charset="utf-8">
<title>Dabwell Kids – In-App Icon Set</title>
<link href="https://fonts.googleapis.com/css2?family=Schoolbell&display=swap" rel="stylesheet">
<style>
  :root{
    --board:#dce3ec;
    --screen:#8a9db3;
    --panel:#e3e8ee;
    --ink:#1d1d1f;
    --btn-light:#eceef1;
    --btn-edge:#b7bcc3;
    --glyph:#7b8087;
    --btn-dark:#7c8086;
    --white:#ffffff;
  }
  html,body{margin:0;padding:0;overflow:hidden;background:var(--board);}
  .board{width:1200px;height:1200px;display:block;}
  .hand{font-family:'Schoolbell',cursive;fill:var(--ink);}
  .note{font-size:22px;}
  .heading{font-size:30px;}
  .label{font-size:32px;}
  .brand{font-family:'Schoolbell',cursive;font-size:46px;fill:var(--ink);}
  .arrow{fill:none;stroke:var(--ink);stroke-width:2.4;stroke-linecap:round;}
  .glyph-light{color:var(--glyph);}
  .glyph-dark{color:var(--white);}
</style>
</head>
<body>
<svg class="board" viewBox="0 0 1200 1200" xmlns="http://www.w3.org/2000/svg">
  <defs>
    <marker id="tip" viewBox="0 0 10 10" refX="8" refY="5" markerWidth="7" markerHeight="7" orient="auto">
      <path d="M0 0 L10 5 L0 10 Z" fill="#1d1d1f"/>
    </marker>
    <linearGradient id="paintTones" x1="0" y1="0" x2="1" y2="0">
      <stop offset="0" stop-color="#c7643d"/>
      <stop offset="0.35" stop-color="#b97045"/>
      <stop offset="0.55" stop-color="#3aa6a0"/>
      <stop offset="0.75" stop-color="#3a7fd0"/>
      <stop offset="1" stop-color="#2f55c4"/>
    </linearGradient>

    <!-- icon glyphs, drawn on a 100×100 grid in currentColor -->
    <symbol id="g-brush" viewBox="0 0 100 100">
      <path d="M48 14 C60 32 64 46 60 56 Q48 66 36 56 C32 46 36 32 48 14Z" fill="currentColor"/>
      <rect x="40" y="62" width="16" height="8" rx="2" fill="currentColor"/>
      <rect x="42" y="72" width="12" height="18" rx="3" fill="currentColor"/>
      <path d="M72 16 L75 25 L84 28 L75 31 L72 40 L69 31 L60 28 L69 25Z" fill="currentColor"/>
    </symbol>
    <symbol id="g-options" viewBox="0 0 100 100">
      <circle cx="34" cy="40" r="13" fill="currentColor"/>
      <circle cx="34" cy="40" r="17" fill="none" stroke="currentColor" stroke-width="7" stroke-dasharray="6 7.3"/>
      <circle cx="66" cy="60" r="15" fill="currentColor"/>
      <circle cx="66" cy="60" r="19" fill="none" stroke="currentColor" stroke-width="8" stroke-dasharray="7 7.9"/>
    </symbol>
    <symbol id="g-home" viewBox="0 0 100 100">
      <path d="M22 50 L50 24 L78 50 V78 Q78 82 74 82 H26 Q22 82 22 78Z" fill="currentColor"/>
    </symbol>
    <symbol id="g-reset" viewBox="0 0 100 100">
      <path d="M26 20 H62 L76 34 V80 H26Z" fill="none" stroke="currentColor" stroke-width="7" stroke-linejoin="round"/>
      <path d="M40 50 L62 72 M62 50 L40 72" stroke="currentColor" stroke-width="7" stroke-linecap="round"/>
    </symbol>
    <symbol id="g-undo" viewBox="0 0 100 100">
      <path d="M76 78 Q76 46 44 46" fill="none" stroke="currentColor" stroke-width="16" stroke-linecap="round"/>
      <path d="M20 46 L46 24 V68Z" fill="currentColor"/>
    </symbol>
    <symbol id="g-redo" viewBox="0 0 100 100">
      <path d="M24 78 Q24 46 56 46" fill="none" stroke="currentColor" stroke-width="16" stroke-linecap="round"/>
      <path d="M80 46 L54 24 V68Z" fill="currentColor"/>
    </symbol>
    <symbol id="g-share" viewBox="0 0 100 100">
      <path d="M38 40 H28 V80 H72 V40 H62" fill="none" stroke="currentColor" stroke-width="7" stroke-linejoin="round"/>
      <path d="M50 60 V20" stroke="currentColor" stroke-width="7" stroke-linecap="round"/>
      <path d="M36 32 L50 16 L64 32" fill="none" stroke="currentColor" stroke-width="7" stroke-linecap="round" stroke-linejoin="round"/>
    </symbol>
  </defs>

  <!-- ===== Main app screen ===== -->
  <g class="app-screen">
    <rect x="196" y="94" width="808" height="608" fill="var(--screen)"/>
    <rect class="painting-area" x="300" y="250" width="660" height="420" rx="60" fill="url(#paintTones)"
          role="img" aria-label="Rainbow of thick painted brush strokes above a rounded paint palette with black, red, green, blue and empty wells"/>

    <!-- clean brush button + brush width slider -->
    <circle cx="240" cy="125" r="19" fill="var(--btn-dark)"/>
    <use href="#g-brush" x="225" y="110" width="30" height="30" class="glyph-dark"/>
    <path d="M233 152 L240 160 L247 152Z" fill="var(--panel)"/>
    <rect x="215" y="160" width="46" height="185" rx="4" fill="var(--panel)"/>
    <circle cx="238" cy="173" r="4" fill="none" stroke="var(--glyph)" stroke-width="1.6"/>
    <rect x="234" y="185" width="8" height="128" rx="4" fill="var(--glyph)"/>
    <circle cx="238" cy="241" r="7" fill="var(--white)" stroke="var(--glyph)" stroke-width="1.6"/>
    <circle cx="238" cy="328" r="7" fill="none" stroke="var(--glyph)" stroke-width="1.6"/>

    <!-- options button + drop-down menu -->
    <circle cx="961" cy="126" r="19" fill="var(--btn-dark)"/>
    <use href="#g-options" x="946" y="111" width="30" height="30" class="glyph-dark"/>
    <path d="M954 152 L961 160 L968 152Z" fill="var(--panel)"/>
    <rect x="938" y="160" width="46" height="206" rx="4" fill="var(--panel)"/>
    <g class="menu-items">
      <circle cx="961" cy="187" r="15" fill="var(--btn-light)" stroke="var(--btn-edge)"/>
      <use href="#g-home" x="949" y="175" width="24" height="24" class="glyph-light"/>
      <circle cx="961" cy="225" r="15" fill="var(--btn-dark)"/>
      <use href="#g-reset" x="949" y="213" width="24" height="24" class="glyph-dark"/>
      <circle cx="961" cy="263" r="15" fill="var(--btn-light)" stroke="var(--btn-edge)"/>
      <use href="#g-undo" x="949" y="251" width="24" height="24" class="glyph-light"/>
      <circle cx="961" cy="301" r="15" fill="var(--btn-light)" stroke="var(--btn-edge)"/>
      <use href="#g-redo" x="949" y="289" width="24" height="24" class="glyph-light"/>
      <circle cx="961" cy="339" r="15" fill="var(--btn-light)" stroke="var(--btn-edge)"/>
      <use href="#g-share" x="949" y="327" width="24" height="24" class="glyph-light"/>
    </g>
  </g>

  <!-- ===== Annotations ===== -->
  <g class="annotations">
    <text class="hand note" x="296" y="78" transform="rotate(-4 296 78)">Clean Brush</text>
    <text class="hand note" x="296" y="104" transform="rotate(-4 296 104)">(select mode)</text>
    <path class="arrow" d="M284 72 Q256 72 242 92" marker-end="url(#tip)"/>

    <text class="hand note" x="795" y="86" transform="rotate(-3 795 86)">Options</text>
    <text class="hand note" x="771" y="112" transform="rotate(-3 771 112)">(select mode)</text>
    <path class="arrow" d="M910 70 Q944 72 952 96" marker-end="url(#tip)"/>

    <g transform="rotate(-4 410 230)">
      <text class="hand note" x="338" y="193">Long press to</text>
      <text class="hand note" x="334" y="222">bring out scale</text>
      <text class="hand note" x="332" y="251">for brush width</text>
    </g>
    <path class="arrow" d="M324 198 Q294 198 278 214" marker-end="url(#tip)"/>

    <text class="hand note" x="846" y="190">Home</text>
    <text class="hand note" x="849" y="220">Reset</text>
    <text class="hand note" x="773" y="246">(select mode)</text>
    <text class="hand note" x="849" y="280">Undo</text>
    <text class="hand note" x="851" y="315">Redo</text>
    <text class="hand note" x="848" y="351">Share</text>
    <path class="arrow" d="M914 176 Q926 166 940 172" marker-end="url(#tip)"/>
    <path class="arrow" d="M910 220 Q922 210 936 215" marker-end="url(#tip)"/>
    <path class="arrow" d="M910 264 Q922 254 936 258" marker-end="url(#tip)"/>
    <path class="arrow" d="M910 300 Q922 290 936 295" marker-end="url(#tip)"/>
    <path class="arrow" d="M910 336 Q922 326 936 331" marker-end="url(#tip)"/>

    <g transform="rotate(-4 1090 240)">
      <text class="hand note" x="1012" y="215">Brings out drop</text>
      <text class="hand note" x="1014" y="244">down menu</text>
      <text class="hand note" x="1018" y="273">when selected</text>
    </g>
    <path class="arrow" d="M1032 186 Q1002 184 986 198" marker-end="url(#tip)"/>
  </g>

  <!-- ===== Brand ===== -->
  <text class="brand" x="78" y="842">Dabwell Kids</text>

  <!-- ===== Clean interface preview ===== -->
  <g class="preview">
    <rect x="74" y="948" width="264" height="198" fill="var(--screen)"/>
    <rect x="110" y="1000" width="200" height="120" rx="22" fill="url(#paintTones)"
          role="img" aria-label="Small view of the painting screen with rainbow strokes and paint palette"/>
    <circle cx="87" cy="958" r="5" fill="var(--btn-dark)"/>
    <circle cx="323" cy="958" r="5" fill="var(--btn-dark)"/>

    <circle cx="440" cy="885" r="72" fill="#f3f5f8"/>
    <clipPath id="zoomClip"><circle cx="440" cy="885" r="72"/></clipPath>
    <rect x="368" y="853" width="118" height="104" fill="var(--screen)" clip-path="url(#zoomClip)"/>
    <circle cx="431" cy="893" r="24" fill="var(--btn-dark)"/>
    <use href="#g-options" x="412" y="874" width="38" height="38" class="glyph-dark"/>
    <path class="arrow" d="M394 904 Q352 900 330 930" marker-end="url(#tip)"/>

    <text class="hand label" x="406" y="1012">Clean</text>
    <text class="hand label" x="382" y="1052">Interface</text>
  </g>

  <!-- ===== Icon set ===== -->
  <g class="icon-set">
    <text class="hand heading" x="546" y="810">Simple &amp; Kid-Friendly Icons</text>
    <text class="hand heading" x="550" y="856">(with active select mode)</text>

    <path d="M626 918 L636 910 V926Z" fill="#eef1f5"/>
    <rect x="636" y="896" width="247" height="62" rx="4" fill="#eef1f5"/>
    <circle cx="653" cy="927" r="5" fill="none" stroke="var(--glyph)" stroke-width="1.6"/>
    <rect x="667" y="921" width="174" height="12" rx="6" fill="var(--glyph)"/>
    <circle cx="744" cy="927" r="9" fill="var(--white)" stroke="var(--glyph)" stroke-width="1.6"/>
    <circle cx="861" cy="927" r="10" fill="none" stroke="var(--glyph)" stroke-width="1.6"/>

    <circle cx="979" cy="921" r="53" fill="var(--btn-dark)"/>
    <use href="#g-brush" x="937" y="879" width="84" height="84" class="glyph-dark"/>
    <circle cx="1103" cy="921" r="53" fill="var(--btn-dark)"/>
    <use href="#g-options" x="1061" y="879" width="84" height="84" class="glyph-dark"/>

    <circle cx="598" cy="1080" r="53" fill="var(--btn-light)" stroke="var(--btn-edge)" stroke-width="1.5"/>
    <use href="#g-home" x="564" y="1046" width="68" height="68" class="glyph-light"/>
    <circle cx="722" cy="1080" r="53" fill="var(--btn-dark)"/>
    <use href="#g-reset" x="688" y="1046" width="68" height="68" class="glyph-dark"/>
    <circle cx="850" cy="1080" r="53" fill="var(--btn-light)" stroke="var(--btn-edge)" stroke-width="1.5"/>
    <use href="#g-undo" x="816" y="1046" width="68" height="68" class="glyph-light"/>
    <circle cx="976" cy="1080" r="53" fill="var(--btn-light)" stroke="var(--btn-edge)" stroke-width="1.5"/>
    <use href="#g-redo" x="942" y="1046" width="68" height="68" class="glyph-light"/>
    <circle cx="1102" cy="1080" r="53" fill="var(--btn-light)" stroke="var(--btn-edge)" stroke-width="1.5"/>
    <use href="#g-share" x="1068" y="1046" width="68" height="68" class="glyph-light"/>
  </g>
</svg>
</body>
</html>
```